Create a business Card for a Women Owned Business Body Positive Company. The winner we hope to work with on other projects coming up for grand opening for flyers, postcards, email marketing, facebook page, stationary, labels, tshirt design....
We would like if possible in the background of the card a infinity symbol or crown if it fits into the design if not it's ok. But I am open to all suggestions we had alot problems with the our new logo being created this time sad to say :(

Our colors are Royal Purple, Grey, Black Thank you in advance for your talent, you hard work and your submissions!
Delia and Nadine :)
Updates

my Logo is velvet harbor boutique which is purple and has a heart and infinity sign in it and my colors are purple silver and black only of another card i had done nothing else. My logo is VELVET HARBOR BOUTIQUE LOGO

Industry/Entity Type

Retail

Contact Information for Business Card

website: www.velvtharborboutiques.example email: sales@velvetharborboutique.example
Delia Pruett & Nadine Kolb Owners

Font styles to use
Script

Colors
b768aa

Requirements
Must have
• COLORS ARE PURPLE BLACK AND GREY
Nice to have
• INFINITY SIGNING IN THE BACKGROUND

```html
<!DOCTYPE html>
<html lang="en">
<head>
<meta charset="utf-8">
<title>Velvet Harbor Boutique – Business Card</title>
<link rel="stylesheet" href="https://fonts.googleapis.com/css2?family=Great+Vibes&family=Marcellus&family=Quattrocento:wght@400&display=swap">
<style>
  :root {
    --backdrop: #b4b4b4;
    --purple: #5a2d78;
    --purple-deep: #4b2366;
    --lavender: #ece3f2;
    --silver: #ececec;
    --silver-edge: #a9a9ad;
    --ink-purple: #5b2b7a;
    --rule: #3a3a3a;
  }
  * { margin: 0; padding: 0; box-sizing: border-box; }
  html, body {
    width: 1200px; height: 576px; overflow: hidden;
    background: var(--backdrop);
  }
  .canvas { position: relative; width: 1200px; height: 576px; }
  .card {
    position: absolute; width: 484px; height: 293px;
    border-radius: 12px; overflow: hidden;
    box-shadow: 0 2px 6px rgba(0,0,0,.25);
  }
  .card--front {
    left: 82px; top: 139px;
    background: linear-gradient(180deg, var(--purple) 0%, var(--purple-deep) 100%);
  }
  .front-pattern {
    position: absolute; inset: 0;
    background: linear-gradient(180deg, rgba(255,255,255,.04), rgba(255,255,255,.02));
  }
  .front-wordmark {
    position: absolute; left: 0; right: 0; top: 150px;
    text-align: center; color: var(--lavender);
    font-family: "Marcellus", serif;
  }
  .front-wordmark__name { font-size: 30px; line-height: 1; letter-spacing: .5px; }
  .front-wordmark__sub { font-size: 12px; letter-spacing: 5px; margin-top: 6px; }
  .card--back { left: 602px; top: 138px; background: var(--silver); }
  .card--back svg { position: absolute; inset: 0; }
  .owners {
    position: absolute; left: 20px; top: 36px; color: var(--lavender);
  }
  .owners__names { font-family: "Great Vibes", cursive; font-size: 24px; line-height: 1; }
  .owners__role { font-family: "Quattrocento", serif; font-size: 11px; margin-top: 9px; }
  .contact {
    position: absolute; left: 20px; top: 219px; list-style: none;
    font-family: "Quattrocento", serif; font-size: 13px; color: var(--lavender);
  }
  .contact li { display: flex; align-items: center; gap: 9px; height: 17px; }
  .contact svg { position: static; flex: none; }
</style>
</head>
<body>
<main class="canvas">
  <section class="card card--front" aria-label="Card front">
    <div class="front-pattern" role="img" aria-label="Faint repeating ornamental pattern"></div>
    <div class="front-wordmark">
      <div class="front-wordmark__name">VELVET HARBOR</div>
      <div class="front-wordmark__sub">BOUTIQUE</div>
    </div>
  </section>

  <section class="card card--back" aria-label="Card back">
    <svg width="484" height="293" viewBox="0 0 484 293">
      <path d="M0 0 H340 C290 80 292 205 338 293 H0 Z" fill="var(--silver-edge)"/>
      <path d="M0 0 H327 C280 80 282 205 326 293 H0 Z" fill="var(--purple)"/>
      <g transform="translate(402 146) rotate(90)" font-family="Marcellus, serif" fill="var(--ink-purple)" text-anchor="middle">
        <text x="0" y="0" font-size="27">VELVET HARBOR</text>
        <text x="0" y="24" font-size="11" letter-spacing="5" fill="var(--rule)">BOUTIQUE</text>
      </g>
      <g stroke="var(--rule)" stroke-width="1.2">
        <line x1="424" y1="52" x2="424" y2="95"/>
        <line x1="424" y1="197" x2="424" y2="240"/>
      </g>
    </svg>
    <div class="owners">
      <div class="owners__names">Delia Pruett &amp; Nadine Kolb</div>
      <div class="owners__role">owners</div>
    </div>
    <ul class="contact">
      <li>
        <svg width="11" height="8" viewBox="0 0 11 8" aria-hidden="true"><rect x=".5" y=".5" width="10" height="7" fill="none" stroke="currentColor"/><path d="M.5 .5 L5.5 4.5 L10.5 .5" fill="none" stroke="currentColor"/></svg>
        sales@velvetharborboutique.example
      </li>
      <li>
        <svg width="11" height="11" viewBox="0 0 11 11" aria-hidden="true"><circle cx="5.5" cy="5.5" r="5" fill="none" stroke="currentColor"/><ellipse cx="5.5" cy="5.5" rx="2.2" ry="5" fill="none" stroke="currentColor"/><line x1=".5" y1="5.5" x2="10.5" y2="5.5" stroke="currentColor"/></svg>
        www.velvtharborboutiques.example
      </li>
    </ul>
  </section>
</main>
</body>
</html>
```